Copperfield Kitchen - Menu

I want a redesign of our menu. The theme is rustic industrial. I need to be able to fir the pizza offering on the first page. I would like an option with a black background as well. I have attached our CURRENT menu "Copperfield Kitchen" as well as some other samples I like

Target Market(s)

Guests

Industry/Entity Type

Restaurant

Font styles to use
Other font styles liked:
• Fonts can include: Rockwell, Myriad Pro, Playfair Display Bold, Playfair Display

Colors
0054AA
0677BA
7BADD7
CADEEF
E8F1F8
EE7325
F08F49
F5BC92
FAE3D3
FDF4ED

Requirements
Should not have
• Our brand colors are: Black, White, red orange and Navy

```html
<!DOCTYPE html>
<html lang="en">
<head>
<meta charset="utf-8">
<title>Copperfield Kitchen – Menu</title>
<link href="https://fonts.googleapis.com/css2?family=Bebas+Neue&family=Archivo+Narrow:wght@500;700&family=Old+Standard+TT:ital,wght@0,400;0,700;1,400&display=swap" rel="stylesheet">
<style>
:root{
  --paper:#FBEEE6;
  --orange:#E8722A;
  --orange-soft:#F08F49;
  --peach:#F5BC92;
  --ink:#3B3A38;
  --dark:#2A2A2A;
  --white:#FFFFFF;
}
*{margin:0;padding:0;box-sizing:border-box}
html,body{width:776px;height:1200px;overflow:hidden;background:var(--paper)}
.menu{position:relative;width:776px;height:1200px;overflow:hidden;background:var(--paper);color:var(--ink);font-family:"Old Standard TT",serif;font-size:7px;line-height:1.15}
.abs{position:absolute}
.head{font-family:"Bebas Neue",sans-serif;color:var(--orange);font-weight:400;line-height:.9}
.name{font-family:"Archivo Narrow",sans-serif;font-weight:700;text-transform:uppercase}

/* brand */
.brand{left:0;width:776px;top:66px;text-align:center;color:var(--orange)}
.brand .est{font-family:"Archivo Narrow",sans-serif;font-weight:700;font-size:9px;letter-spacing:1px;display:flex;justify-content:center;align-items:center;gap:8px}
.brand .est i{display:inline-block;width:12px;height:12px;border-radius:50%;background:var(--orange)}
.brand .word{font-family:"Bebas Neue",sans-serif;font-size:50px;line-height:.95;letter-spacing:1px;margin-top:4px}
.brand .sub{font-family:"Bebas Neue",sans-serif;font-size:22px;letter-spacing:2px;border-top:2px solid var(--orange);display:inline-block;padding-top:3px;margin-top:2px}

/* starters */
.starters{left:81px;top:190px;width:200px;height:226px;border:1px solid var(--peach);padding:12px 10px}
.starters .head{font-size:31px;text-align:center;margin-bottom:6px}
.starter{display:flex;justify-content:space-between;color:var(--orange);margin-bottom:4px}
.starter .name{font-size:8.5px;font-weight:500}
.starter p{font-size:7px;color:var(--orange);padding-left:8px;width:155px;line-height:1.1}
.starter .price{font-size:7.5px}

/* burgers */
.burgers{left:293px;top:190px;width:402px;height:225px;border:1px solid var(--peach);padding:10px 11px}
.burgers .head{font-size:25px;width:160px;line-height:.85}
.sides-note{font-size:5.5px;text-transform:uppercase;margin-top:6px;color:var(--ink)}
.sides-grid{display:grid;grid-template-columns:48px 70px;font-size:5.5px;margin:2px 0 10px}
.item{display:flex;justify-content:space-between;margin-bottom:8px}
.item .name{font-size:7.5px}
.item p{font-size:6.5px;padding-left:8px}
.col-l{position:absolute;left:11px;top:100px;width:175px}
.col-r{position:absolute;left:206px;top:26px;width:178px}
.addon-box{position:absolute;left:206px;top:152px;width:100px;height:56px;background:var(--dark);color:var(--white);font-size:4.8px;text-transform:uppercase;padding:5px 6px;line-height:1.2}
.burger-art{left:592px;top:322px;width:130px;height:148px;border-radius:60px 60px 26px 26px;background:linear-gradient(180deg,#F5BC92,#E8722A)}

/* soups */
.soups{left:92px;top:450px;width:232px;height:428px;border:6px solid var(--orange);border-bottom:none;border-radius:28px 28px 0 0;padding:14px 18px;text-align:center}
.soups .head{font-size:28px;margin-bottom:1px}
.salad .name{font-size:9.5px;display:block}
.salad .price{font-family:"Old Standard TT",serif;font-size:9px;display:block;margin:3px 0 1px}
.salad p{font-size:8.5px;line-height:1.05;margin-bottom:9px}
.small-row{display:flex;justify-content:space-between;font-size:8.5px;text-align:left}
.small-row .name{font-size:9px}
.salad-art{position:absolute;left:10px;right:10px;bottom:0;height:48px;background:linear-gradient(180deg,#FAE3D3,#F5BC92)}
.soups-note{left:78px;top:893px;width:260px;text-align:center;font-size:7px;color:var(--orange);text-transform:uppercase}

/* mains */
.mains-word{left:294px;top:540px;width:150px;height:70px;transform:rotate(-90deg) scaleX(1.15);transform-origin:center;font-size:100px;text-align:center}
.mains{left:416px;top:455px;width:206px}
.mains .item{margin-bottom:15px}
.mains .item .name{font-size:8.5px}
.mains .item p{font-size:7.5px}
.mains .sides-grid{grid-template-columns:74px 74px 40px;font-size:5.8px;margin-bottom:2px}
.mains .sides-note{font-size:6px;margin-top:0}
.mains .crisp{font-style:italic;font-size:5.8px;margin-bottom:13px}
.mains-rule{left:333px;top:705px;width:290px;border-top:1px solid var(--orange)}
.preset{left:348px;top:718px;width:268px}
.preset .sides-note{font-size:6.5px;margin-bottom:4px}
.preset .name{font-size:9px}
.preset p{font-size:8px;padding-left:10px}
.preset small{display:block;font-size:5.5px;font-style:italic;padding-left:20px}
.pizza-art{left:352px;top:825px;width:248px;height:76px;clip-path:polygon(0 85%,80% 0,100% 20%,12% 100%);background:linear-gradient(90deg,#F5BC92,#E8722A)}

/* add it on */
.addon{left:646px;top:488px;width:62px;height:416px;border-left:1px solid var(--orange-soft)}
.addon .head{font-size:21px;text-align:center;line-height:.95;padding-left:6px}
.addon-lines{position:absolute;left:-145px;top:203px;width:360px;height:46px;transform:rotate(-90deg);font-size:7.8px;line-height:11.5px;text-transform:uppercase;white-space:nowrap}

/* pizza */
.pizza-banner{left:42px;top:918px;width:585px;display:flex;align-items:center;gap:8px}
.pizza-banner .try{font-size:20px;line-height:.85}
.pizza-banner .big{font-size:55px}
.pizza-banner .after{font-family:"Bebas Neue",sans-serif;font-size:23px;line-height:.95;letter-spacing:.4px;color:var(--ink)}
.pizza-icon{left:632px;top:912px;width:82px;height:60px;background:linear-gradient(135deg,#F5BC92,#E8722A);clip-path:polygon(0 100%,40% 20%,100% 0,70% 70%)}
.cards{left:34px;top:982px;display:flex;gap:8px}
.card{position:relative;width:135px;height:106px;border:1px solid var(--orange-soft);border-radius:6px;text-align:center;padding:12px 6px 0}
.card h3{font-family:"Bebas Neue",sans-serif;font-weight:400;font-size:17px;line-height:.95;color:var(--ink);margin-bottom:4px}
.card p{font-size:8px;line-height:1.05}
.card .price{position:absolute;left:55px;bottom:-9px;width:22px;height:22px;border-radius:50%;background:var(--peach);border:2px solid var(--paper);font-size:7px;font-weight:700;display:flex;align-items:center;justify-content:center}

/* footer */
.footer{left:0;top:1123px;width:776px;height:77px;background:var(--orange);color:#3a2010}
.footer .fine{position:absolute;left:34px;top:28px;width:410px;font-size:5.2px;font-style:italic}
.footer .fine p{margin-bottom:4px}
.care{position:absolute;left:480px;top:16px;width:270px}
.care h4{font-family:"Archivo Narrow",sans-serif;font-size:10px;color:var(--white);margin-bottom:3px}
.care-row{display:flex;gap:10px;font-family:"Archivo Narrow",sans-serif;font-size:5px;color:var(--white);align-items:center}
.care-row span{display:flex;align-items:center;gap:3px}
.care-row i{display:inline-block;width:14px;height:14px;border-radius:50%;background:var(--peach)}
.care-row i.sq{border-radius:2px;width:22px}
.care .risk{font-size:5px;font-style:italic;margin-top:3px}
</style>
</head>
<body>
<main class="menu">

  <header class="brand abs">
    <div class="est"><span>Est.</span><i></i><span>2016</span></div>
    <div class="word">COPPERFIELD</div>
    <div class="sub">KITCHEN</div>
  </header>

  <section class="starters abs">
    <h2 class="head">STARTERS</h2>
    <div class="starter"><div><span class="name">MARA'S GRILLED AVOCADO</span><p>stuffed with shrimp salad, topped with chipotle aioli and served with housemade tortilla chips</p></div><span class="price">17</span></div>
    <div class="starter"><div><span class="name">WINGS</span><p>honey sriracha, buffalo, or BBQ</p></div><span class="price">13</span></div>
    <div class="starter"><div><span class="name">DEVILISH EGGS</span><p>(four) topped with candied bacon, chives and tangy BBQ</p></div><span class="price">8</span></div>
    <div class="starter"><div><span class="name">NACHOS</span><p>housemade cheese sauce, black beans, jalapeños, sour cream and guacamole ADD: PORK OR CHICKEN 4</p></div><span class="price">13</span></div>
    <div class="starter"><div><span class="name">CRISPY BRUSSELS</span><p>tossed in white truffle oil ADD: FRIED EGG 1.5</p></div><span class="price">10</span></div>
    <div class="starter"><div><span class="name">DYNAMITE SHRIMP</span><p>lightly battered fried shrimp tossed in a sweet chili aioli</p></div><span class="price">15</span></div>
  </section>

  <section class="burgers abs">
    <h2 class="head">BURGERS AND SANDWICHES</h2>
    <div class="sides-note">Below items come with a choice of one side:</div>
    <div class="sides-grid">
      <span>golden fries</span><span>smoked potato salad</span>
      <span>black beans</span><span>sweet potato fries (ADD 1)</span>
      <span>coleslaw</span><span>truffle fries (ADD 1.5)</span>
      <span></span><span>onion rings (ADD 2.5)</span>
    </div>
    <div class="col-l">
      <div class="item"><div><span class="name">The Copperfield Burger</span><p>angus burger, caramelized onions, lettuce, tomato, and house spread on a brioche bun<br>*bun contains egg</p></div><span>17</span></div>
      <div class="item"><div><span class="name">Crispy Chicken Sandwich</span><p>havarti, lettuce, tomato and house spread on a french roll</p></div><span>15</span></div>
      <div class="item"><div><span class="name">The Dip</span><p>slow roasted tri-tip on a french roll served with au jus and a side of creamed horseradish</p></div><span>20</span></div>
    </div>
    <div class="col-r">
      <div class="item"><div><span class="name">BLT</span><p>thick cut applewood bacon, lettuce, tomato, and house spread on toasted sourdough</p></div><span>15</span></div>
      <div class="item"><div><span class="name">The Verdant Burger</span><p>patty made entirely from plants, caramelized onions, lettuce, tomato, and house spread</p></div><span>18</span></div>
      <div class="item"><div><span class="name">Grilled Cheese</span><p>blend of jack, cheddar and swiss, caramelized onions, and mustard horseradish on sourdough garlic bread<br>ADD: CUP TOMATO SOUP 4</p></div><span>15</span></div>
    </div>
    <div class="addon-box">Add to above sandwiches:<br>American, cheddar, havarti, swiss, jack, pepper jack, blue cheese or<br>fried egg 1.5<br>bacon or avocado 2.5</div>
  </section>
  <div class="burger-art abs" role="img" aria-label="Engraved-style illustration of a stacked burger"></div>

  <section class="soups abs">
    <h2 class="head">SOUPS &amp; SALADS</h2>
    <div class="salad"><span class="name">Seasonal Chopped</span><span class="price">16</span><p>rotisserie chicken, romaine, avocado, beans, broccoli, feta cheese, cucumber, and roasted red peppers, tossed in our house vinaigrette</p></div>
    <div class="salad"><span class="name">Greens &amp; Goats</span><span class="price">15</span><p>mixed greens, beets, red onions, dried cranberries, candied pecans and goat cheese tossed in our housemade raspberry vinaigrette</p></div>
    <div class="salad"><span class="name">Kale Chicken Caesar</span><span class="price">15</span><p>kale, romaine, rotisserie chicken, toasted chickpeas, cherry tomatoes, tossed in housemade caesar dressing and parmesan cheese</p></div>
    <div class="salad"><span class="name">Kale Chicken Caesar</span><span class="price">15</span><p>blue cheese crumbles, chives, tomatoes, and bacon with topped with blue cheese dressing</p></div>
    <div class="small-row"><span class="name">Garden Side Salad</span><span>6</span></div>
    <div class="small-row"><span class="name">Side Caesar Salad</span><span>6</span></div>
    <div class="small-row"><span class="name">Tomato Soup</span><span>cup 5 / bowl 7</span></div>
    <div class="salad-art" role="img" aria-label="Engraved-style illustration of a salad bowl"></div>
  </section>
  <div class="soups-note abs">Add to above salads: fried egg 1.5 · grilled salmon 10</div>

  <h2 class="head mains-word abs">MAINS</h2>
  <section class="mains abs">
    <div class="sides-note">Below entrees come with<br>a choice of two sides:</div>
    <div class="sides-grid"><span>sautéed vegetables</span><span>whipped potatoes</span><span>coleslaw</span><span>farro pilaf</span><span>smoked potato salad</span><span>black beans</span></div>
    <div class="crisp">crispy brussels sprouts tossed in truffle oil (ADD 2)</div>
    <div class="item"><div><span class="name">St. Louis Ribs</span><p>pork ribs slow cooked and glazed with BBQ sauce</p></div><span>24</span></div>
    <div class="item"><div><span class="name">Salmon Filet</span><p>fresh Atlantic salmon topped with a citrus beurre blanc</p></div><span>27</span></div>
    <div class="item"><div><span class="name">Garlic Shrimp</span><p>sautéed in herb butter</p></div><span>22</span></div>
    <div class="item"><div><span class="name">Rotisserie Chicken</span><p>bone in breast with a caper salsa</p></div><span>20</span></div>
    <div class="item"><div><span class="name">Flat Iron</span><p>drizzled with chimichurri sauce</p></div><span>28</span></div>
  </section>
  <div class="mains-rule abs"></div>
  <section class="preset abs">
    <div class="sides-note">Below entrees come with preselected sides:</div>
    <div class="item"><div><span class="name">St. Louis Ribs</span><p>served with housemade tortilla chips, black beans and salsas</p>
      <small>CHICKEN: guacamole, sour cream and cotija cheese</small>
      <small>SHRIMP: guacamole and chipotle aioli sauce</small>
      <small>PULLED PORK: onions, cilantro, green chili aioli and cotija cheese</small></div><span>15</span></div>
    <div class="item"><div><span class="name">Farro Fried Rice</span><p>farro pilaf, egg, brussels, carrot, celery and shallots in a sesame tamari glaze with dynamite aioli on the side</p></div><span>15</span></div>
  </section>
  <div class="pizza-art abs" role="img" aria-label="Engraved-style illustration of a pizza slice"></div>

  <aside class="addon abs">
    <h2 class="head">ADD<br>IT ON</h2>
    <div class="addon-lines">
      · Golden fries 7 · Truffle fries 9 · Sweet potato fries 7<br>
      · Coleslaw 4 · Fully loaded fries 7 · Onion rings 7 · Black beans 5<br>
      · Whipped potatoes 3.5 · Farro pilaf 5 · Sautéed vegetables 6<br>
      · Smoked potato salad 4 · Mac-n-cheese (bacon &amp; herb crumbs) 9
    </div>
  </aside>

  <div class="pizza-banner abs">
    <div class="head try">TRY<br>OUR</div>
    <div class="head big">12" ARTISAN PIZZA</div>
    <div class="after">AFTER 4:00PM (TAKE OUR<br>DOUGH TO-GO IN MARKET!)</div>
  </div>
  <div class="pizza-icon abs" role="img" aria-label="Small illustration of a pizza slice on a server"></div>

  <section class="cards abs">
    <article class="card"><h3>WHITE<br>TRUFFLE</h3><p>garlic oil, fresh mozzarella, parmesan, white truffle oil and fresh cracked pepper</p><span class="price">19</span></article>
    <article class="card"><h3>BUFFALO<br>CHICKEN RANCH</h3><p>tomato sauce, buffalo chicken roasted cherry tomatoes, cheese blend, housemade ranch and cilantro</p><span class="price">21</span></article>
    <article class="card"><h3>VERDANT<br>BURGER SAUSAGE</h3><p>tomato sauce, dried tomatoes, verdant burger sausage, fresh mozzarella, cheese blend, parmesan</p><span class="price">22</span></article>
    <article class="card"><h3>VEGGIE</h3><p>tomato sauce, zucchini, yellow squash, mushroom, feta cheese and pickled red onions</p><span class="price">20</span></article>
    <article class="card"><h3>CHEESE</h3><p>tomato sauce, fresh mozzarella, cheese blend</p><span class="price">17</span></article>
  </section>

  <footer class="footer abs">
    <div class="fine">
      <p>*We are concerned with your well-being. If you have any allergies, please alert us. We cannot guarantee food allergens will not be transferred through cross contamination or manufacturing methods</p>
      <p>5% Operational Surcharge will be added to each check. This fee is intended to be equitably distributed amongst our operational increases as a result of increased vendors and supplier costs. This is not a gratuity for services provided. Thank you for your continued support!</p>
    </div>
    <div class="care">
      <h4>WE CARE!</h4>
      <div class="care-row">
        <span><i class="sq"></i>ALL-NATURAL FRESH<br>AND PREPARED MEATS</span>
        <span><i></i>LOCALLY RAISED AND<br>FREE RANGE CHICKEN</span>
        <span><i></i>ALL EGGS<br>CAGE FREE</span>
      </div>
      <div class="risk">*The consumption of raw or undercooked meats, eggs, seafood or shellfish may increase your risk of foodborne illness</div>
    </div>
  </footer>

</main>
</body>
</html>
```